Professional WordPress Website Design & Development for IT Consulting Company (Quennor)

We are an IT consulting company (Quennor) based in Germany and are looking for a professional, modern and scalable WordPress website design INCLUDING full coding (WordPress theme/template).

IMPORTANT:
We do NOT want only a design (eg Photoshop files).
We want a fully working, coded WordPress website that we can host and manage ourselves.

The uploaded files (PowerPoint, HTML, logo) are ONLY for rough orientation.
They do NOT represent the final structure but give an idea of our visual style.

---

## COMPANY STRUCTURE (IMPORTANT)

Currently we operate as:

* Quennor UG (limited liability)

Planned structure:

* Quennor Operations GmbH (main operating company)
* Quennor Holding GmbH
* optionally later: Quennor Capital GmbH

The website should be designed as a scalable group website, but currently focus on the main brand "Quennor".

---

## BUSINESS FOCUS (IMPORTANT)

Our main business is:
→ Managed Services (core focus)

Additional areas:

* IT Infrastructure (Virtanode, Cytrel, Hyper-V)
* Windows Server/Client environments
* Cloud & Hybrid solutions
* Network, Firewall, VPN
* Data center operations, migrations and rollouts

The website should clearly communicate:
→ reliability, scalability, enterprise-level service quality

---

## DESIGN STYLE & VISUAL DIRECTION

We like the design direction from our uploaded PowerPoint.

IMPORTANT:

* We especially like the green checkered/grid-style background with dark/black gradient
* This style should be used as inspiration
* Colors: green + dark/black + modern IT style

Design should be:

* modern
* clean
* professional
* enterprise-level
* trustworthy
* not playful or overloaded

---

## TECHNICAL REQUIREMENTS

* WordPress (self-hosted)
* Full source code delivery (no proprietary lock-in)
* Custom theme or clean reusable theme
* Editable without developer
* Multilingual: German, English, Polish
* SEO-friendly
* Fast performance
* GDPR/DSVO compliant contact form

---

## RESPONSIVE DESIGN & ACCESSIBILITY

Must be optimized for:

* Desktop
* Tablet
* Mobile

Layout must adapt automatically.

Accessibility:

* Clear typography
* Good contrast
* Easy navigation
* Mobile-friendly usability

Mobile experience must be fully functional and professional.

---

## STRUCTURE (NO ONE-PAGE WEBSITE)

We want a structured website with pages and subpages.

MAIN NAVIGATION (HEADER):

* Home
* Managed Services (MAIN FOCUS)
* Services
* Solutions / Expertise
* Projects / News
* Resources
* Careers
* Company
* Contact

SUBNAVIGATION / SUBPAGES (examples):

Managed Services:

* Overview
* Service Models
* SLAs & Support
* Monitoring & Operations

Services:

* Virtanode
* Cytrel
* Hyper-V
* Windows Server / Client
* SCCM / Intune
* Network / Firewall / VPN

Solutions:

* Data Center
* Cloud / Hybrid
* Migration Projects
* Security / Zero Trust

Projects / News:

* Projects
* Opportunities
* Articles

Resources:

* Available Experts
* Freelancer / Partner
* Internal Staff

Careers:

* Open Positions
* Freelancer Opportunities

Company:

* About Us
* Group Structure
* Values
* References

---

## HEADER / FOOTER STRUCTURE

HEADER:

* Sticky header (always visible)
* Main navigation with dropdowns or mega menu
* Clean, structured layout

FOOTER:

* Legal pages (Imprint, Privacy, Terms)
* Contact information
* Possibly quick links
* Consistent across all pages

---

## SPECIAL FEATURES

1. PROJECT / NEWS SYSTEM

* publish projects
* project opportunities
* articles

2. RESOURCE SYSTEM

* freelancers
* partners
* internal staff

With:

* skills
* availability
* role
* location
* language

---

## IMAGES, ICONS & LICENSING

Stock images (eg iStock) may be used as placeholders.

IMPORTANT:

* We will purchase final licenses ourselves
* No Google images or unknown sources

Icons and illustrations are welcome but must be properly licensed.

At delivery:

* Full asset list required (images, icons, sources, licenses)

---

## DELIVERABLES

We expect:

* Fully working WordPress website
* Full source code
* Installation instructions
* Plugin list
* No hidden dependencies
* No forced subscriptions
* Full usage rights

---

## IMPORTANT

We want to pay ONCE and fully own everything.

---

## LANGUAGES

Content will be managed by us:

* German
* English
* Polish

---

## FILES

Uploaded files are only for inspiration.

---

We are looking for a long-term, scalable and professional solution suitable for enterprise customers.
Updates

Additional update regarding interactions, hover effects and animations:

HOVER EFFECTS

We would like to include subtle and modern hover effects across the website:

Cards (eg Open Positions, Projects): → slight green glow on hover → minimal lift effect (approx. 2–4px)

Navigation (header): → hover color should be green (NOT orange)

Footer links (Imprint, Privacy, Terms): → slightly brighter on hover

Social icons (Linkora, XING, Gigstrelo): → subtle glow and slight scale on hover

IMPORTANT: All hover effects must be consistent, clean and not exaggerated.

ACTIVE STATE (VERY IMPORTANT)

Navigation elements must clearly show when they are active (current page).

This applies to:

Header navigation footer left

Behavior:

Active links should remain highlighted (eg green color and/or subtle underline) Users should always clearly see which page they are currently on

IMPORTANT: Active and hover states must be visually consistent across the entire website.

ANIMATIONS / MICRO INTERACTIONS

The website should not feel static.

We would like subtle and professional animations, such as:

smooth transitions between elements minimal background movement (very subtle) soft UI interactions

IMPORTANT: No heavy, flashy or distracting animations.

The goal is a high-end, enterprise-level feel.

COUNTERS / KEY METRICS

We want animated key numbers, for example:

150+ clients 10+ years experience 24/7 support 99.9% uptime

Behavior:

numbers should count up when they come into view (on scroll) fast and smoothly (approx. 0. 5–1 seconds) animation should trigger only once

Overall goal: A modern, dynamic and high-quality website with subtle interactions, not a flashy or overloaded design.

Hi everyone,

I have uploaded additional reference files to give you a clearer idea of the direction we are aiming for.

IMPORTANT: These files are only meant as inspiration and guidance – they are NOT strict templates that must be copied 1:1.

What we particularly like:

Dark / black + green design Subtle grid / tech background (as seen in the PowerPoint) Clean, modern and professional enterprise IT style Structured layout (no one-page scrolling) LANGUAGE FLAGS (IMPORTANT UPDATE)

Please adjust the language selection as follows:

Order:

German (DE) English (EN) Polish (PL)

For ENGLISH: We do NOT want a standard flag.

Instead, please create a combined UK/US flag:

Diagonally split design One side showing the UK flag The other side showing the US flag

This should look clean and professional (not playful).

FOOTER (IMPORTANT)

Footer should be:

Minimal and clean (not large or heavy) Positioned at the very bottom

Include:

Legal Notice / Imprint / Privacy Policy / Data Protection / Terms and Conditions / Terms

And: © Quennor UG

Social icons:

Linkora XING Gigstrelo

Please remove:

Facebook Twitter Instagram LAYOUT NOTE

Please avoid duplicate sections (eg "About Us" appearing multiple times).

We prefer a clean and structured layout with clear sections.

Thank you very much – looking forward to your designs!

Ich brauche zusätzliche Tage um durchzusehen

Target Market(s)

Enterprise and mid-sized companies, especially in automotive, finance, technology and IT infrastructure environments.

Industry/Entity Type

IT Consulting / Managed Services / Enterprise IT

Coding

Coded - Design and coding required

Font styles to use
Sans Serif

Colors
0094D4
00A9DD
6FCCEA
C7EBF8
E9F6FB
00AB8E
00BBA5
67D7C9
C6EFE9
E9F9F6
59FF00
82FF00
B8FF75
E3FFCB
F4FFEA

Requirements
Must have
• - Fully coded WordPress website (not just design) - Self-hosted, no dependency on designer - Responsive (desktop, tablet, mobile) - Multilingual (German, English, Polish) - Editable without developer - Clean, modern enterprise design - Structured navigation with subpages (no one-page website) - GDPR-compliant contact form - Scalable structure for future company expansion (group structure)
Nice to have
• - Subtle modern animations (not overloaded) - Mega menu or structured dropdown navigation - Clean icon set and optional illustrations - Reusable page templates - Fast loading performance - SEO-friendly structure - Team presentation with profiles (management, internal staff, technical roles) - Integration of social links (Linkora, Xing, Gigstrelo)
Should not have
• - No one-page scrolling website - No overly colorful or playful design - No outdated or generic templates - No confusing or complex navigation - No cheap-looking stock-heavy layouts - No dependency on proprietary builders or subscriptions

```html
<!DOCTYPE html>
<html lang="en">
<head>
<meta charset="utf-8">
<title>About Quennor</title>
<link href="https://fonts.googleapis.com/css2?family=Space+Grotesk:wght@500;700&family=Inter:wght@400;500;600&family=JetBrains+Mono:wght@400;500&display=swap" rel="stylesheet">
<style>
:root{
  --bg:#0a0b0d;
  --band:#131824;
  --card:#0d0e11;
  --line:#1d2029;
  --text:#f3f4f6;
  --muted:#a3a8b3;
  --dim:#6b7280;
  --green:#7fd62a;
  --green-soft:#1a2410;
  --heading:"Space Grotesk",sans-serif;
  --body:"Inter",sans-serif;
  --mono:"JetBrains Mono",monospace;
}
*{box-sizing:border-box;margin:0;padding:0}
html,body{width:1200px;height:2490px;overflow:hidden}
body{background:var(--bg);color:var(--text);font-family:var(--body);position:relative}
.wrap{width:1027px;margin:0 auto;position:relative}
.eyebrow{font-family:var(--mono);font-size:9px;letter-spacing:1.5px;color:var(--green);text-transform:uppercase}
.title{font-family:var(--heading);font-weight:700;text-transform:uppercase;letter-spacing:-.5px;line-height:1;white-space:nowrap}

/* header */
.site-header{position:absolute;top:0;left:0;width:1200px;height:46px;display:flex;align-items:center;padding:0 26px;z-index:2}
.brand{display:flex;align-items:center;gap:9px}
.brand-mark{width:22px;height:22px;background:var(--green);border-radius:3px}
.brand-name{font-family:var(--body);font-weight:600;font-size:20px;color:var(--green);line-height:1}
.main-nav{position:absolute;left:50%;transform:translateX(-50%);display:flex;gap:23px;font-family:var(--mono);font-size:10px;letter-spacing:.8px;color:var(--muted)}
.main-nav .active{color:var(--green);border-bottom:1px solid var(--green);padding-bottom:2px}
.header-actions{margin-left:auto;display:flex;align-items:center;gap:24px}
.lang{display:flex;align-items:center;gap:6px;font-family:var(--mono);font-size:10px;color:var(--muted)}
.btn{display:inline-flex;align-items:center;gap:7px;border-radius:6px;font-family:var(--body);font-weight:500}
.btn-primary{background:var(--green);color:#0b0f06}
.btn-ghost{border:1px solid #2c2f38;color:var(--text)}
.book{height:30px;padding:0 17px;font-size:10px}

/* hero */
.hero{height:459px;position:relative;background:
  linear-gradient(rgba(127,214,42,.035) 1px,transparent 1px) 0 0/58px 58px,
  linear-gradient(90deg,rgba(127,214,42,.035) 1px,transparent 1px) 0 0/58px 58px,
  var(--bg)}
.hero-copy{position:absolute;left:83px;top:156px;width:370px}
.hero-copy h1{font-size:50px;margin:10px 0 20px}
.hero-copy p{font-size:11.5px;line-height:1.65;color:var(--muted);margin-bottom:16px}
.hero-photo{position:absolute;left:619px;top:116px;width:491px;height:276px;border-radius:8px;
  background:linear-gradient(135deg,#5b5d60 0%,#2a2b2d 45%,#8a8c8e 75%,#3a3b3d 100%)}

/* stats */
.stats{height:272px;background:var(--band);padding-top:68px}
.stat-grid{display:grid;grid-template-columns:repeat(3,1fr);gap:23px}
.stat-card{height:136px;background:var(--card);border:1px solid var(--line);border-radius:8px;text-align:center;padding-top:22px}
.stat-value{font-family:var(--heading);font-weight:700;font-size:32px;margin-top:10px;line-height:1}
.stat-unit{font-family:var(--mono);font-size:9px;letter-spacing:1px;color:var(--muted);font-weight:400;margin-left:4px}
.stat-card p{font-size:9.5px;color:#c8ccd3;margin-top:12px}

/* principles */
.principles{height:387px;text-align:center;padding-top:73px}
.principles h2,.team h2,.certs h2{font-size:38px;margin-top:14px}
.card-grid{display:grid;grid-template-columns:repeat(3,1fr);gap:23px;margin-top:60px;text-align:left}
.value-card{height:127px;background:var(--card);border:1px solid var(--line);border-radius:8px;padding:22px 23px 16px}
.value-card h3{font-size:13px;font-weight:600;margin:8px 0 6px;line-height:1.2}
.value-card p{font-size:11px;line-height:1.5;color:var(--muted)}
.value-card.fading{opacity:.55}

/* team */
.team{height:417px;background:#0d0f13;text-align:center;padding-top:72px}
.team-card{height:175px;background:var(--card);border:1px solid var(--line);border-radius:8px;padding:22px 23px}
.icon-badge{width:45px;height:45px;border-radius:50%;background:var(--green-soft);display:flex;align-items:center;justify-content:center}
.team-card h3{font-size:13px;font-weight:600;margin:15px 0 6px}
.team-card .role{font-family:var(--mono);font-size:9px;letter-spacing:1px;color:var(--green)}
.team-card p{font-size:9.5px;line-height:1.5;color:var(--muted);margin-top:12px}
.team .card-grid{margin-top:48px}

/* certs */
.certs{height:350px;text-align:center;padding-top:72px}
.cert-grid{display:grid;grid-template-columns:repeat(4,1fr);gap:17px 17px;margin-top:37px;text-align:left}
.cert{height:37px;border:1px solid var(--line);border-radius:6px;display:flex;align-items:center;gap:10px;padding-left:12px;font-size:10px;color:#d4d7dd}

/* cta */
.cta{height:381px;text-align:center;padding-top:107px}
.cta h2{font-size:38px}
.cta p{font-size:11.5px;color:var(--muted);margin-top:18px}
.cta-actions{display:flex;justify-content:center;gap:12px;margin-top:18px}
.cta-actions .btn{height:33px;padding:0 17px;font-size:11.5px}

/* footer */
.site-footer{position:absolute;left:0;top:2166px;width:1200px;height:324px;background:var(--band);padding:50px 26px 0}
.footer-cols{display:grid;grid-template-columns:297px 296px 297px 1fr}
.footer-about p{font-size:11px;line-height:1.7;color:#c4c8cf;margin-top:16px}
.socials{display:flex;gap:10px;margin-top:18px}
.social{width:28px;height:28px;border-radius:50%;background:#1d222e;display:flex;align-items:center;justify-content:center}
.social span{width:8px;height:8px;border-radius:50%;background:#9aa0ab}
.footer-col h4{font-family:var(--mono);font-size:9px;letter-spacing:1.2px;color:var(--muted);font-weight:500;margin-top:4px}
.footer-col ul{list-style:none;margin-top:11px}
.footer-col li{font-size:10px;color:var(--muted);line-height:25px}
.footer-bottom{position:absolute;left:26px;right:26px;top:273px;display:flex;justify-content:space-between;font-size:10px;color:var(--muted)}
</style>
</head>
<body>

<header class="site-header">
  <div class="brand">
    <span class="brand-mark"></span>
    <span class="brand-name">Quennor</span>
  </div>
  <nav class="main-nav">
    <span>Services</span><span>Solutions</span><span class="active">Company</span><span>Contact</span>
  </nav>
  <div class="header-actions">
    <span class="lang">
      <svg width="11" height="11" viewBox="0 0 24 24" fill="none" stroke="currentColor" stroke-width="2"><circle cx="12" cy="12" r="10"/><path d="M2 12h20M12 2a15 15 0 0 1 0 20M12 2a15 15 0 0 0 0 20"/></svg>EN
    </span>
    <span class="btn btn-primary book">Book a call</span>
  </div>
</header>

<section class="hero">
  <div class="hero-copy">
    <div class="eyebrow">Company</div>
    <h1 class="title">About Quennor</h1>
    <p>We're a team of infrastructure consultants and operators based in Germany, serving mid-market and enterprise clients across Europe.</p>
    <p>We believe in building IT that just works—so you can focus on what matters. No fluff, no unnecessary complexity. Just reliable, well-designed infrastructure that supports your business goals.</p>
  </div>
  <div class="hero-photo" role="img" aria-label="Black and white photo of the team working together at desks in a bright city office"></div>
</section>

<section class="stats">
  <div class="wrap stat-grid">
    <div class="stat-card">
      <svg width="26" height="26" viewBox="0 0 24 24" fill="none" stroke="var(--green)" stroke-width="2" stroke-linecap="round"><circle cx="12" cy="12" r="10"/><path d="M12 6v6l4 2"/></svg>
      <div class="stat-value">10+<span class="stat-unit">YEARS</span></div>
      <p>Delivering IT operations and projects</p>
    </div>
    <div class="stat-card">
      <svg width="26" height="26" viewBox="0 0 24 24" fill="none" stroke="var(--green)" stroke-width="2" stroke-linecap="round"><circle cx="9" cy="7" r="4"/><path d="M2 21v-2a4 4 0 0 1 4-4h6a4 4 0 0 1 4 4v2M16 3.1a4 4 0 0 1 0 7.8M22 21v-2a4 4 0 0 0-3-3.9"/></svg>
      <div class="stat-value">150+<span class="stat-unit">CLIENTS</span></div>
      <p>Across manufacturing, logistics, and professional services</p>
    </div>
    <div class="stat-card">
      <svg width="26" height="26" viewBox="0 0 24 24" fill="none" stroke="var(--green)" stroke-width="2" stroke-linecap="round"><path d="M3 18v-6a9 9 0 0 1 18 0v6"/><rect x="3" y="14" width="4" height="7" rx="1.5"/><rect x="17" y="14" width="4" height="7" rx="1.5"/></svg>
      <div class="stat-value">24/7<span class="stat-unit">SUPPORT</span></div>
      <p>Monitoring and incident response</p>
    </div>
  </div>
</section>

<section class="principles">
  <div class="wrap">
    <div class="eyebrow">Our principles</div>
    <h2 class="title">What we stand for</h2>
    <div class="card-grid">
      <div class="value-card">
        <svg width="24" height="24" viewBox="0 0 24 24" fill="none" stroke="var(--green)" stroke-width="2"><circle cx="12" cy="12" r="10"/><circle cx="12" cy="12" r="6"/><circle cx="12" cy="12" r="2"/></svg>
        <h3>Clear Communication</h3>
        <p>No jargon, no surprises. We keep you informed at every step.</p>
      </div>
      <div class="value-card fading">
        <svg width="24" height="24" viewBox="0 0 24 24" fill="none" stroke="var(--green)" stroke-width="2" stroke-linecap="round"><path d="M9 18h6M10 22h4M12 2a7 7 0 0 0-4 12.7V16h8v-1.3A7 7 0 0 0 12 2z"/></svg>
        <h3>Documented Decisions</h3>
        <p>Every choice is recorded, every change is tracked.</p>
      </div>
      <div class="value-card fading">
        <svg width="24" height="24" viewBox="0 0 24 24" fill="none" stroke="var(--green)" stroke-width="2" stroke-linecap="round"><path d="M4 12l4-4 4 2 4-2 4 4-7 7z"/></svg>
        <h3>Long-term Partnerships</h3>
        <p>We grow with our clients, building relationships that last.</p>
      </div>
    </div>
  </div>
</section>

<section class="team">
  <div class="wrap">
    <div class="eyebrow">Our team</div>
    <h2 class="title">The people behind Quennor</h2>
    <div class="card-grid">
      <div class="team-card">
        <div class="icon-badge"><svg width="20" height="20" viewBox="0 0 24 24" fill="none" stroke="var(--green)" stroke-width="2" stroke-linecap="round"><circle cx="9" cy="7" r="4"/><path d="M2 21v-2a4 4 0 0 1 4-4h6a4 4 0 0 1 4 4v2M16 3.1a4 4 0 0 1 0 7.8M22 21v-2a4 4 0 0 0-3-3.9"/></svg></div>
        <h3>Leadership Team</h3>
        <div class="role">STRATEGIC DIRECTION</div>
        <p>Experienced IT executives with decades of combined experience in enterprise infrastructure.</p>
      </div>
      <div class="team-card">
        <div class="icon-badge"><svg width="20" height="20" viewBox="0 0 24 24" fill="none" stroke="var(--green)" stroke-width="2" stroke-linecap="round"><circle cx="9" cy="7" r="4"/><path d="M2 21v-2a4 4 0 0 1 4-4h6a4 4 0 0 1 4 4v2M16 3.1a4 4 0 0 1 0 7.8M22 21v-2a4 4 0 0 0-3-3.9"/></svg></div>
        <h3>Technical Consultants</h3>
        <div class="role">SOLUTION DESIGN</div>
        <p>Certified experts in cloud, virtualization, security, and networking technologies.</p>
      </div>
      <div class="team-card">
        <div class="icon-badge"><svg width="20" height="20" viewBox="0 0 24 24" fill="none" stroke="var(--green)" stroke-width="2" stroke-linecap="round"><circle cx="9" cy="7" r="4"/><path d="M2 21v-2a4 4 0 0 1 4-4h6a4 4 0 0 1 4 4v2M16 3.1a4 4 0 0 1 0 7.8M22 21v-2a4 4 0 0 0-3-3.9"/></svg></div>
        <h3>Operations Team</h3>
        <div class="role">24/7 SUPPORT</div>
        <p>Dedicated professionals ensuring your systems run smoothly around the clock.</p>
      </div>
    </div>
  </div>
</section>

<section class="certs">
  <div class="wrap">
    <div class="eyebrow">Expertise</div>
    <h2 class="title">Certified professionals</h2>
    <div class="cert-grid">
      <div class="cert"><svg width="13" height="13" viewBox="0 0 24 24" fill="none" stroke="var(--green)" stroke-width="2.4" stroke-linecap="round"><circle cx="12" cy="12" r="10"/><path d="M8 12l3 3 5-6"/></svg>Veltrasoft Gold Partner</div>
      <div class="cert"><svg width="13" height="13" viewBox="0 0 24 24" fill="none" stroke="var(--green)" stroke-width="2.4" stroke-linecap="round"><circle cx="12" cy="12" r="10"/><path d="M8 12l3 3 5-6"/></svg>Virtanode Professional</div>
      <div class="cert"><svg width="13" height="13" viewBox="0 0 24 24" fill="none" stroke="var(--green)" stroke-width="2.4" stroke-linecap="round"><circle cx="12" cy="12" r="10"/><path d="M8 12l3 3 5-6"/></svg>Corvexa Certified</div>
      <div class="cert"><svg width="13" height="13" viewBox="0 0 24 24" fill="none" stroke="var(--green)" stroke-width="2.4" stroke-linecap="round"><circle cx="12" cy="12" r="10"/><path d="M8 12l3 3 5-6"/></svg>Nimbra Cloud Partner</div>
      <div class="cert"><svg width="13" height="13" viewBox="0 0 24 24" fill="none" stroke="var(--green)" stroke-width="2.4" stroke-linecap="round"><circle cx="12" cy="12" r="10"/><path d="M8 12l3 3 5-6"/></svg>Celestra Expert</div>
      <div class="cert"><svg width="13" height="13" viewBox="0 0 24 24" fill="none" stroke="var(--green)" stroke-width="2.4" stroke-linecap="round"><circle cx="12" cy="12" r="10"/><path d="M8 12l3 3 5-6"/></svg>Cytrel Certified</div>
      <div class="cert"><svg width="13" height="13" viewBox="0 0 24 24" fill="none" stroke="var(--green)" stroke-width="2.4" stroke-linecap="round"><circle cx="12" cy="12" r="10"/><path d="M8 12l3 3 5-6"/></svg>Servora Certified</div>
      <div class="cert"><svg width="13" height="13" viewBox="0 0 24 24" fill="none" stroke="var(--green)" stroke-width="2.4" stroke-linecap="round"><circle cx="12" cy="12" r="10"/><path d="M8 12l3 3 5-6"/></svg>SecuNorm 27001</div>
    </div>
  </div>
</section>

<section class="cta">
  <h2 class="title">Want to join the team?</h2>
  <p>We're always looking for talented people who share our passion for great IT.</p>
  <div class="cta-actions">
    <span class="btn btn-primary"><svg width="12" height="12" viewBox="0 0 24 24" fill="none" stroke="currentColor" stroke-width="2.2"><rect x="3" y="4" width="18" height="18" rx="2"/><path d="M16 2v4M8 2v4M3 10h18"/></svg>Get in touch</span>
    <span class="btn btn-ghost">View our services<svg width="11" height="11" viewBox="0 0 24 24" fill="none" stroke="currentColor" stroke-width="2.4" stroke-linecap="round"><path d="M5 12h14M13 6l6 6-6 6"/></svg></span>
  </div>
</section>

<footer class="site-footer">
  <div class="footer-cols">
    <div class="footer-about">
      <div class="brand">
        <span class="brand-mark"></span>
        <span class="brand-name">Quennor</span>
      </div>
      <p>IT consulting and managed services.<br>Based in Germany, serving Europe.</p>
      <div class="socials">
        <span class="social" aria-label="Linkora"><span></span></span>
        <span class="social" aria-label="Chirpex"><span></span></span>
        <span class="social" aria-label="Info"><svg width="12" height="12" viewBox="0 0 24 24" fill="none" stroke="#9aa0ab" stroke-width="2" stroke-linecap="round"><circle cx="12" cy="12" r="10"/><path d="M12 8v5M12 16h.01"/></svg></span>
      </div>
    </div>
    <div class="footer-col">
      <h4>SERVICES</h4>
      <ul><li>Managed Services</li><li>Cloud &amp; Hybrid</li><li>Modern Workplace</li><li>Security</li><li>Network</li><li>Data Center</li></ul>
    </div>
    <div class="footer-col">
      <h4>COMPANY</h4>
      <ul><li>About Us</li><li>Careers</li><li>References</li><li>Partners</li><li>Contact</li></ul>
    </div>
    <div class="footer-col">
      <h4>LEGAL</h4>
      <ul><li>Imprint</li><li>Privacy Policy</li><li>Terms of Service</li><li>Data Protection</li></ul>
    </div>
  </div>
  <div class="footer-bottom">
    <span>© 2026 Quennor UG. All rights reserved.</span>
    <span>Made with precision in Germany</span>
  </div>
</footer>

</body>
</html>
```